Highlight Document Over Image for Slide

We are seeking a graphic designer to overlay a news article on an image that pertains to the article, aiming for a stylish yet professional appearance. Given the limited resources, we encourage you to use your imagination and go beyond what basic tools like PowerPoint can offer.

```html
<!DOCTYPE html>
<html lang="en">
<head>
<meta charset="utf-8">
<title>20 — Introduction or Possession of Contraband Items</title>
<link rel="stylesheet" href="https://fonts.googleapis.com/css2?family=Arimo:wght@400;700&display=swap">
<style>
  :root {
    --land-dry: #b39a68;
    --land-mid: #9c8a63;
    --built: #7d766a;
    --built-dark: #6a645a;
    --water: #6a6a62;
    --water-deep: #5d5e58;
    --band: rgba(88, 90, 89, 0.9);
    --text: #ffffff;
    --muted: #dcdcdc;
    --rule: #e6e6e6;
  }
  * { margin: 0; padding: 0; box-sizing: border-box; }
  html, body { width: 1200px; height: 772px; overflow: hidden; background: var(--water); }
  .slide {
    position: relative;
    width: 1200px;
    height: 772px;
    overflow: hidden;
    font-family: "Arimo", Arial, sans-serif;
    color: var(--text);
  }
  .aerial-backdrop {
    position: absolute;
    inset: 0;
    background:
      radial-gradient(ellipse 300px 260px at 540px 370px, rgba(112,104,92,0.95) 0%, rgba(112,104,92,0.6) 55%, rgba(112,104,92,0) 100%),
      radial-gradient(ellipse 260px 200px at 190px 260px, rgba(150,135,105,0.85) 0%, rgba(150,135,105,0) 100%),
      radial-gradient(ellipse 420px 170px at 780px 60px, rgba(185,160,105,0.9) 0%, rgba(185,160,105,0) 100%),
      radial-gradient(ellipse 380px 200px at 1020px 170px, rgba(120,112,90,0.85) 0%, rgba(120,112,90,0) 100%),
      radial-gradient(ellipse 520px 330px at 1080px 560px, var(--water) 0%, rgba(106,106,98,0) 100%),
      radial-gradient(ellipse 360px 220px at 120px 560px, var(--water-deep) 0%, rgba(93,94,88,0) 100%),
      linear-gradient(170deg, var(--land-dry) 0%, var(--land-mid) 30%, var(--built) 55%, var(--water) 75%, var(--water-deep) 100%);
  }
  .caption-band {
    position: absolute;
    left: 0; right: 0;
    top: 690px;
    bottom: 0;
    background: var(--band);
  }
  .rule-number {
    position: absolute;
    left: 706px;
    top: 496px;
    font-size: 124px;
    font-weight: 700;
    line-height: 1;
    letter-spacing: -2px;
  }
  .rule-title {
    position: absolute;
    left: 853px;
    top: 507px;
    font-size: 27.5px;
    font-weight: 700;
    line-height: 33.5px;
    letter-spacing: 0.2px;
    text-transform: uppercase;
  }
  .rule-text {
    position: absolute;
    left: 35px;
    top: 618px;
    width: 1140px;
    font-size: 18.2px;
    line-height: 24px;
    font-weight: 400;
  }
  .footer-rule {
    position: absolute;
    left: 0;
    top: 751px;
    width: 1140px;
    height: 1px;
    background: var(--rule);
  }
  .page-number {
    position: absolute;
    left: 1155px;
    top: 740px;
    font-size: 19px;
    color: var(--muted);
  }
</style>
</head>
<body>
  <main class="slide">
    <div class="aerial-backdrop" role="img" aria-label="Aerial map view of a waterfront correctional facility with surrounding streets, parking and bay shoreline"></div>
    <div class="caption-band"></div>

    <div class="rule-number">20</div>
    <h1 class="rule-title">Introduction or<br>possession of<br>contraband items</h1>

    <p class="rule-text">
      Employees shall not introduce or possess unauthorized items such as escape paraphernalia, weapons, facsimiles of weapons,<br>
      ammunition, wireless communication devices, cell phones, tobacco or facsimiles of tobacco products (e.g. electronic vapor<br>
      cigarettes), lighters or any other item not specifically authorized by PD 04.04.100 "Custody, Security and Safety Systems<br>
      (Exempt)", OP 04.04.100 "Gate Security" or facility operating procedure in any facility where offenders are housed.<br>
      Employees are responsible for any item in their possession.
    </p>

    <div class="footer-rule"></div>
    <div class="page-number">36</div>
  </main>
</body>
</html>
```